Landing page for www.vorndale.dk

A landing page for Clickrank.

Text on the advertisement is:
"efficient website
Price is dkr. 3495,-
We create a design before you say yes.
LANDINGPAGE URL"

Design should lean up against the one on www.vorndale.dk

But the following rules for making landing pages applies:
1. Only one headline
2. Form in the middle of it all
3. The landing page must be relevant to the clickrankadvertisement text.
4. Very little other text, catchphrases etc. If any must be setup in bulletpoints.

Target Market(s)

Small companies, new entrepenuers.

Requirements
Must have
• One headline
Form in the middle
other text bulletpointed.
Relevant to the clickrank advertisement
Nice to have
• Focus on the form
Should not have
• anything that removes focus from the form.

```html
<!DOCTYPE html>
<html lang="en">
<head>
<meta charset="utf-8">
<title>Vorndale – Efficient website for only dkr. 3495,-</title>
<link rel="stylesheet" href="https://fonts.googleapis.com/css2?family=Ubuntu:wght@500;700&family=Arimo:wght@400;700&display=swap">
<style>
:root{
  --red:#d8141b;
  --red-dark:#a80d0d;
  --orange:#f25a0e;
  --ink:#2f2f2f;
  --muted:#b5b5b5;
  --line:#d6d6d6;
  --band-top:#ffffff;
  --band-bottom:#ececec;
  --footer-top:#3c3c3c;
  --footer-bottom:#1f1f1f;
  --footer-text:#d9d9d9;
  --tick:#5cb82e;
}
*{box-sizing:border-box;margin:0;padding:0}
html,body{width:1200px;height:894px;overflow:hidden}
body{position:relative;background:#fff;font-family:"Arimo",Helvetica,Arial,sans-serif;color:var(--ink)}
.hero{position:absolute;left:0;top:0;width:1200px;height:385px;
  background:linear-gradient(#fff 0%,#f7f7f7 45%,var(--band-bottom) 100%);
  border-bottom:4px solid #dedede}
.headline{position:absolute;left:0;width:1200px;top:34px;text-align:center;
  font-family:"Ubuntu",sans-serif;font-weight:500;font-size:41px;color:var(--red);letter-spacing:.5px}
.tagline{position:absolute;left:0;width:1200px;top:99px;text-align:center;
  font-family:"Ubuntu",sans-serif;font-weight:500;font-size:20px;color:var(--ink);letter-spacing:.6px}
.tagline .brand{color:var(--red)}
.form-panel{position:absolute;left:412px;top:163px;width:374px;height:226px;
  background:linear-gradient(#fff,#f6f6f6 70%,#fff);
  box-shadow:0 -2px 6px rgba(0,0,0,.18)}
.ribbon{position:absolute;left:525px;top:156px;width:138px;height:54px}
.ribbon-label{position:absolute;left:525px;top:168px;width:138px;text-align:center;
  font-weight:700;font-size:15px;color:#fff;letter-spacing:.3px}
.field{position:absolute;left:438px;width:323px;height:31px;background:#fff;
  border:1px solid var(--line);border-radius:3px;box-shadow:inset 0 1px 3px rgba(0,0,0,.08);
  font-size:15px;color:var(--muted);padding:7px 10px}
.field-name{top:223px}
.field-email{top:266px}
.submit{position:absolute;left:558px;top:324px;width:204px;height:30px;border:1px solid #cfcfcf;border-radius:3px;
  background:linear-gradient(#fafafa,#e3e3e3);font-size:15px;color:#222;padding:6px 0 0 13px;letter-spacing:.3px}
.submit svg{position:absolute;left:161px;top:7px}
.section-title{position:absolute;top:429px;font-size:15px;color:#222;letter-spacing:.3px}
.features-title{left:240px}
.designs-title{left:604px}
.features{list-style:none;position:absolute;left:245px;top:469px}
.features li{position:relative;padding-left:28px;height:30px;font-size:12.5px;line-height:15px;color:#222;letter-spacing:.2px}
.features li svg{position:absolute;left:0;top:-2px}
.showcase{position:absolute;left:591px;top:457px;width:412px;height:233px;background:#f4f4f4}
.showcase-shot{position:absolute;left:16px;top:6px;width:376px;height:224px;border:1px solid #bdbdbd;
  background:linear-gradient(135deg,#fafafa 0%,#eeeeee 45%,#9bb07c 65%,#5f8a3b 100%)}
.slide-arrow{position:absolute;top:541px;width:38px;height:38px}
.slide-prev{left:597px}
.slide-next{left:954px}
.footer{position:absolute;left:0;top:748px;width:1200px;height:146px;
  background:linear-gradient(var(--footer-top),var(--footer-bottom));border-top:2px solid #555}
.company{position:absolute;left:207px;top:9px;font-size:9.5px;line-height:15px;color:var(--footer-text);letter-spacing:.4px}
.footer-nav{position:absolute;left:594px;top:16px;font-size:10px;color:var(--footer-text);letter-spacing:.4px}
.footer-brand{position:absolute;left:927px;top:11px;font-family:"Ubuntu",sans-serif;font-weight:500;font-size:17px;color:#e6e6e6;letter-spacing:1px}
</style>
</head>
<body>
<header class="hero">
  <h1 class="headline">Efficient website for only dkr. 3495,-</h1>
  <p class="tagline"><span class="brand">VORNDALE</span> create the design before you say yes.</p>
</header>

<section class="form-panel"></section>
<svg class="ribbon" viewBox="0 0 138 54" aria-hidden="true">
  <defs><linearGradient id="rib" x1="0" y1="0" x2="0" y2="1"><stop offset="0" stop-color="#f5641a"/><stop offset="1" stop-color="#a80d0d"/></linearGradient></defs>
  <path d="M0 30 L6 24 L6 2 L132 2 L132 24 L138 30 L69 54 Z" fill="url(#rib)"/>
  <rect x="6" y="0" width="126" height="4" fill="#8a1a08"/>
</svg>
<div class="ribbon-label">Start Here</div>
<div class="field field-name">Name</div>
<div class="field field-email">Email</div>
<div class="submit">Get your web Now !
  <svg width="12" height="15" viewBox="0 0 12 15" aria-hidden="true"><path d="M1 0 L5 0 L12 7.5 L5 15 L1 15 L8 7.5 Z" fill="var(--red)"/></svg>
</div>

<h2 class="section-title features-title">Get this great features for Dkr. 3495</h2>
<ul class="features">
  <li><svg width="19" height="22" viewBox="0 0 19 22"><rect x="1" y="6" width="15" height="15" rx="2" fill="#fff" stroke="#888"/><path d="M4 12 L8 17 L18 1" fill="none" stroke="var(--tick)" stroke-width="3"/></svg>Content Management Systems (CMS)</li>
  <li><svg width="19" height="22" viewBox="0 0 19 22"><rect x="1" y="6" width="15" height="15" rx="2" fill="#fff" stroke="#888"/><path d="M4 12 L8 17 L18 1" fill="none" stroke="var(--tick)" stroke-width="3"/></svg>Modern &amp; Up to date Designs</li>
  <li><svg width="19" height="22" viewBox="0 0 19 22"><rect x="1" y="6" width="15" height="15" rx="2" fill="#fff" stroke="#888"/><path d="M4 12 L8 17 L18 1" fill="none" stroke="var(--tick)" stroke-width="3"/></svg>Search Engine Optimization (SEO)<br>Unique Concepts</li>
</ul>

<h2 class="section-title designs-title">Our Recent Successful Designs</h2>
<div class="showcase">
  <div class="showcase-shot" role="img" aria-label="Screenshot of a recent client website: a golf design company page with a green golf course photo"></div>
</div>
<svg class="slide-arrow slide-prev" viewBox="0 0 38 38" aria-label="Previous design"><path d="M0 30 L6 38 L6 30 Z" fill="#555"/><rect x="1" y="0" width="36" height="30" rx="3" fill="#fff" stroke="#ccc"/><path d="M22 6 L15 15 L22 24 L18 24 L11 15 L18 6 Z" fill="var(--red-dark)"/></svg>
<svg class="slide-arrow slide-next" viewBox="0 0 38 38" aria-label="Next design"><path d="M38 30 L32 38 L32 30 Z" fill="#555"/><rect x="1" y="0" width="36" height="30" rx="3" fill="#fff" stroke="#ccc"/><path d="M16 6 L23 15 L16 24 L20 24 L27 15 L20 6 Z" fill="var(--red-dark)"/></svg>

<footer class="footer">
  <address class="company" style="font-style:normal">
    Vorndale Ltd.<br>
    CVR: 41 27 58 06 | Tel.: 70 22 41 93 | Address: Lindevej 12, 8000 Aarhus C<br>
    Email: info@vorndale.dk<br>
    Bank: Fjordbank Account number: 4410 0381920657
  </address>
  <nav class="footer-nav">Hjemmesider | Referencer | Produkter | Kontakt | Find os | Bag</nav>
  <div class="footer-brand">VORNDALE</div>
</footer>
</body>
</html>
```